Website for enterprise software start-up

We need a new Wordpress website. We are an early stage start-up focused on mobile video technology for cellular operators. The audience is strategy, marketing and customer acquisition execs from the operators.

The purpose of the site is to act as a sales brochure and capture leads. A demo app can be downloaded from the current site, want to put that behind a contact form.

Current website is at www.brellowmo.tv. Similar number of pages. Looking for a clean design template, with minimal customization. Blog will remain as is.

Want to be able to modify the copy via Wordpress. Reference designs I like: vandrisk.com, tallowquarrymetric.com

Target Market(s)

Mobile operators and MVNOs in the US and Asia Pacific regions

Industry/Entity Type

Business Software

Coding

Coded - Design and coding required

Number of Pages Required

4 page

Font styles to use
Sans Serif

Colors
f78f20

Requirements
Must have
• Form for downloading sample apps.
• Landing page with image, Product, Blog, About, Contact
• Team page

```html
<!DOCTYPE html>
<html lang="en">
<head>
<meta charset="utf-8">
<title>Brellowmo Media</title>
<link href="https://fonts.googleapis.com/css2?family=Raleway:wght@400;500;600;700;800&family=Lato:wght@400;700&display=swap" rel="stylesheet">
<style>
:root{
  --orange:#e2711d;
  --orange-light:#f78f20;
  --ink:#1d1d1d;
  --text:#444;
  --muted:#777;
  --panel:#f2f2f2;
  --white:#fff;
  --dark:#2b2b2b;
  --footer:#333;
}
*{box-sizing:border-box;margin:0;padding:0}
html,body{width:1200px;height:2922px;overflow:hidden}
body{font-family:'Raleway',sans-serif;color:var(--text);background:var(--white)}
.wrap{width:872px;margin:0 auto;position:relative}

/* header */
.site-header{height:86px;background:var(--white);box-shadow:0 1px 3px rgba(0,0,0,.12);position:relative;z-index:2}
.site-header .wrap{display:flex;align-items:center;justify-content:space-between;height:86px;width:888px}
.brand{display:flex;align-items:center;gap:10px;font-weight:800;font-size:36px;color:var(--ink);letter-spacing:-.5px}
.brand-mark{width:52px;height:52px;background:var(--orange)}
.main-nav{display:flex;gap:32px;font-weight:700;font-size:13.5px;color:var(--ink);text-transform:uppercase}
.main-nav a{text-decoration:none;color:inherit;position:relative}
.main-nav a.is-active{color:var(--orange)}
.main-nav a.is-active::before{content:"";position:absolute;left:50%;top:-14px;margin-left:-9px;width:18px;height:3px;background:var(--orange)}

/* hero */
.hero{height:442px;position:relative;background:linear-gradient(100deg,#6f6356 0%,#b9b2a8 35%,#d8d3cc 60%,#8c7e70 100%);text-align:center;color:var(--white)}
.hero-content{position:absolute;left:0;right:0;top:118px}
.hero h1{font-size:35px;font-weight:700;text-shadow:0 2px 4px rgba(0,0,0,.3)}
.hero .rule{width:82px;height:2px;background:var(--orange);margin:14px auto 16px}
.hero p{font-size:19px;line-height:27px;font-weight:500}
.btn{display:inline-block;background:var(--orange);color:var(--white);font-weight:700;font-size:21px;padding:9px 27px;margin-top:24px;text-decoration:none}
.dots{position:absolute;bottom:18px;left:0;right:0;display:flex;justify-content:center;gap:5px}
.dots span{width:11px;height:11px;border-radius:50%;border:2px solid var(--white);background:transparent}
.dots span.on{background:var(--orange)}

/* section titles */
.section-title{text-align:center;font-size:25px;font-weight:700;color:var(--ink);text-transform:uppercase}
.section-title em,.panel-title em{font-style:normal;color:var(--orange)}
.title-rule{width:240px;height:1px;background:#ccc;margin:14px auto 0;position:relative}
.title-rule::after{content:"";position:absolute;left:50%;top:-5px;margin-left:-5px;width:10px;height:10px;border-radius:50%;background:var(--orange)}

/* welcome */
.welcome{height:224px;padding-top:32px}
.welcome p{font-family:'Lato',sans-serif;font-size:11.5px;line-height:21px;text-align:center;color:var(--text);margin-top:28px}

/* feature panels */
.feature{display:flex;height:544px}
.feature.native{height:522px}
.feature-media{width:600px;height:100%}
.feature-media.warm{background:linear-gradient(135deg,#e8b27a 0%,#d98a3a 50%,#c9762a 100%)}
.feature-media.cool{background:linear-gradient(135deg,#5e5e5e 0%,#4a4a4a 50%,#3a3a3a 100%)}
.feature-copy{width:600px;background:var(--panel);padding:36px 0 0 37px}
.feature.native .feature-copy{padding:52px 0 0 164px}
.panel-title{font-size:27px;font-weight:700;color:var(--ink);text-transform:uppercase}
.panel-rule{width:370px;height:1px;background:#cfcfcf;margin:10px 0 18px;position:relative}
.panel-rule::before{content:"";position:absolute;left:0;top:-1px;width:72px;height:3px;background:var(--orange)}
.lead{font-size:15px;font-weight:700;line-height:24px;color:var(--ink);width:400px;letter-spacing:.2px}
.checks{list-style:none;margin-top:20px;width:380px}
.checks li{display:flex;gap:14px;font-family:'Lato',sans-serif;font-size:12.5px;line-height:19px;color:var(--text);margin-bottom:25px}
.checks li svg{flex:0 0 14px;margin-top:2px}
.checks li.short{margin-bottom:17px}

/* clients */
.clients{height:240px;padding-top:43px}
.client-row{display:flex;align-items:center;justify-content:space-between;width:980px;margin:56px auto 0}
.arrow{width:27px;height:29px;background:#8c8c8c;display:flex;align-items:center;justify-content:center}
.client{width:140px;height:68px;border:1px solid #bcbcbc;display:flex;align-items:center;justify-content:center;font-weight:700;font-size:17px;color:#8a8a8a}

/* partner */
.partner{height:210px;background:var(--panel);text-align:center;padding-top:46px}
.badge{width:226px;height:78px;margin:0 auto;background:#dfe3e8;border-radius:6px}
.partner p{font-family:'Lato',sans-serif;font-size:18px;color:var(--ink);margin-top:24px}
.partner p a{color:var(--orange);font-weight:700;text-decoration:none}

/* download */
.download{height:208px;background:linear-gradient(100deg,#3c3532 0%,#5a514b 45%,#6d655e 60%,#3b3431 100%);text-align:center;color:var(--white);padding-top:40px}
.download h2{font-size:23px;font-weight:600}
.stores{display:flex;justify-content:center;gap:33px;margin-top:24px}
.store{width:133px;height:44px;background:#111;border:1px solid #999;border-radius:5px;display:flex;align-items:center;gap:9px;padding-left:14px;font-weight:700;font-size:15px;color:var(--white)}
.store i{width:14px;height:14px;background:var(--white);display:block}

/* contact form */
.contact{height:396px;background:var(--orange);position:relative;padding-top:66px}
.mail-badge{position:absolute;left:50%;top:-36px;margin-left:-40px;width:80px;height:80px;border-radius:50%;background:var(--dark);border:4px solid var(--white);display:flex;align-items:center;justify-content:center}
.lead-form{width:838px;margin:0 auto;display:grid;grid-template-columns:1fr 1fr;gap:12px 24px}
.field{background:var(--panel);height:58px;font-family:'Lato',sans-serif;font-weight:700;font-size:13.5px;color:#555;padding:20px 15px}
.field.wide{grid-column:1 / 3;height:57px}
.field.message{height:117px;padding-top:15px}
.submit{grid-column:1 / 3;justify-self:center;width:102px;height:37px;background:var(--dark);color:var(--white);font-family:'Lato',sans-serif;font-weight:700;font-size:16px;display:flex;align-items:center;justify-content:center;margin-top:4px}

/* footer */
.site-footer{height:50px;background:var(--footer)}
.site-footer .wrap{display:flex;align-items:center;justify-content:space-between;height:50px}
.copyright{font-family:'Lato',sans-serif;font-size:10.5px;color:#ddd}
.social{display:flex;gap:6px}
.social span{width:20px;height:20px;border-radius:50%;display:flex;align-items:center;justify-content:center;font-weight:700;font-size:10px;color:var(--white)}
.social .s1{background:#3b5998}.social .s2{background:#29a9e1}.social .s3{background:#d0422c}.social .s4{background:#1d87bd}
</style>
</head>
<body>

<header class="site-header">
  <div class="wrap">
    <div class="brand"><span class="brand-mark"></span>Brellowmo</div>
    <nav class="main-nav">
      <a class="is-active" href="#">Home</a>
      <a href="#">About Us</a>
      <a href="#">Product</a>
      <a href="#">Our Team</a>
      <a href="#">Blog</a>
      <a href="#">Contact Us</a>
    </nav>
  </div>
</header>

<section class="hero" role="img" aria-label="Photo of a woman lying in bed watching a video on her phone">
  <div class="hero-content">
    <h1>High Quality Mobile Engagement</h1>
    <div class="rule"></div>
    <p>We Engage Mobile Audiences With The Right Video Content<br>At The Perfect Moment</p>
    <a class="btn" href="#">Get Started</a>
  </div>
  <div class="dots"><span class="on"></span><span></span><span></span><span></span></div>
</section>

<section class="welcome">
  <h2 class="section-title">Welcome to <em>Brellowmo Media</em></h2>
  <div class="title-rule"></div>
  <div class="wrap">
    <p>Lorem ipsum dolor sit amet, consectetuer adipiscing elit, sed diam nonummy nibh euismod tincidunt ut laoreet dolore magna aliquam erat volutpat. Ut wisi enim ad minim veniam, quis nostrud exerci tation ullamcorper suscipit lobortis nisl ut aliquip ex ea commodo consequat. Duis autem vel eum iriure dolor in hendrerit in vulputate velit esse molestie consequat, vel illum dolore eu feugiat nulla facilisis at vero eros et accumsan et iusto odio dignissim qui blandit praesent luptatum zzril delenit augue duis dolore tefeugait nulla facilisi.</p>
  </div>
</section>

<section class="feature push">
  <div class="feature-media warm" role="img" aria-label="Phone showing a video push notification on its lock screen over an orange-tinted photo"></div>
  <div class="feature-copy">
    <h2 class="panel-title">Push Video <em>Notifications</em></h2>
    <div class="panel-rule"></div>
    <p class="lead">Personalised flawless HD videos, revealed at the perfect moment, as rich media notifications.</p>
    <ul class="checks">
      <li><svg width="14" height="14" viewBox="0 0 14 14"><rect x="0.75" y="0.75" width="12.5" height="12.5" fill="none" stroke="#e2711d" stroke-width="1.5"/><path d="M3.5 7l2.5 2.5 4.5-5" fill="none" stroke="#e2711d" stroke-width="1.8"/></svg>Reach your mobile audience with beautiful HD thumbnails and in-notification videos.</li>
      <li><svg width="14" height="14" viewBox="0 0 14 14"><rect x="0.75" y="0.75" width="12.5" height="12.5" fill="none" stroke="#e2711d" stroke-width="1.5"/><path d="M3.5 7l2.5 2.5 4.5-5" fill="none" stroke="#e2711d" stroke-width="1.8"/></svg>Instant video playback, zero buffering, guaranteed flawless playback - even when offline.</li>
      <li><svg width="14" height="14" viewBox="0 0 14 14"><rect x="0.75" y="0.75" width="12.5" height="12.5" fill="none" stroke="#e2711d" stroke-width="1.5"/><path d="M3.5 7l2.5 2.5 4.5-5" fill="none" stroke="#e2711d" stroke-width="1.8"/></svg>Content is personalised based on viewer interests and mobile viewing habits.</li>
      <li class="short"><svg width="14" height="14" viewBox="0 0 14 14"><rect x="0.75" y="0.75" width="12.5" height="12.5" fill="none" stroke="#e2711d" stroke-width="1.5"/><path d="M3.5 7l2.5 2.5 4.5-5" fill="none" stroke="#e2711d" stroke-width="1.8"/></svg>Monetize with beautiful HD preroll or interstitial ads.</li>
      <li><svg width="14" height="14" viewBox="0 0 14 14"><rect x="0.75" y="0.75" width="12.5" height="12.5" fill="none" stroke="#e2711d" stroke-width="1.5"/><path d="M3.5 7l2.5 2.5 4.5-5" fill="none" stroke="#e2711d" stroke-width="1.8"/></svg>Easily added to your existing apps within one hour.</li>
    </ul>
  </div>
</section>

<section class="feature native">
  <div class="feature-copy">
    <h2 class="panel-title">Native <em>Push Video</em></h2>
    <div class="panel-rule"></div>
    <p class="lead">Personalised flawless HD videos, discoverable in-app, and playable even when offline.</p>
    <ul class="checks">
      <li><svg width="14" height="14" viewBox="0 0 14 14"><rect x="0.75" y="0.75" width="12.5" height="12.5" fill="none" stroke="#e2711d" stroke-width="1.5"/><path d="M3.5 7l2.5 2.5 4.5-5" fill="none" stroke="#e2711d" stroke-width="1.8"/></svg>Guarantee your audience never gets frustrated with a poor quality mobile videostreaming experience.</li>
      <li><svg width="14" height="14" viewBox="0 0 14 14"><rect x="0.75" y="0.75" width="12.5" height="12.5" fill="none" stroke="#e2711d" stroke-width="1.5"/><path d="M3.5 7l2.5 2.5 4.5-5" fill="none" stroke="#e2711d" stroke-width="1.8"/></svg>Instant video playback, zero buffering, HD quality guaranteed - even when offline.</li>
      <li><svg width="14" height="14" viewBox="0 0 14 14"><rect x="0.75" y="0.75" width="12.5" height="12.5" fill="none" stroke="#e2711d" stroke-width="1.5"/><path d="M3.5 7l2.5 2.5 4.5-5" fill="none" stroke="#e2711d" stroke-width="1.8"/></svg>Content is personalised based on viewer interests and mobile viewing habits.</li>
      <li class="short"><svg width="14" height="14" viewBox="0 0 14 14"><rect x="0.75" y="0.75" width="12.5" height="12.5" fill="none" stroke="#e2711d" stroke-width="1.5"/><path d="M3.5 7l2.5 2.5 4.5-5" fill="none" stroke="#e2711d" stroke-width="1.8"/></svg>Monetize with beautiful HD preroll or interstitial ads.</li>
      <li><svg width="14" height="14" viewBox="0 0 14 14"><rect x="0.75" y="0.75" width="12.5" height="12.5" fill="none" stroke="#e2711d" stroke-width="1.5"/><path d="M3.5 7l2.5 2.5 4.5-5" fill="none" stroke="#e2711d" stroke-width="1.8"/></svg>Use your existing content management and hosting systems.</li>
    </ul>
  </div>
  <div class="feature-media cool" role="img" aria-label="Two phones showing an in-app list of movie trailer videos over a dark photo"></div>
</section>

<section class="clients">
  <h2 class="section-title">Our <em>Clients</em></h2>
  <div class="title-rule"></div>
  <div class="client-row">
    <span class="arrow"><svg width="8" height="12" viewBox="0 0 8 12"><path d="M6.5 1L1.5 6l5 5" fill="none" stroke="#fff" stroke-width="2"/></svg></span>
    <div class="client">Tallis TV</div>
    <div class="client">Ombrix</div>
    <div class="client">Harlow</div>
    <div class="client">Tallis TV</div>
    <div class="client">Wendal Music</div>
    <span class="arrow"><svg width="8" height="12" viewBox="0 0 8 12"><path d="M1.5 1l5 5-5 5" fill="none" stroke="#fff" stroke-width="2"/></svg></span>
  </div>
</section>

<section class="partner">
  <div class="badge" role="img" aria-label="Certified developer partner badge"></div>
  <p><a href="#">Contact Us</a> For Details Of How To Become A Certified Developer Partner.</p>
</section>

<section class="download" role="img" aria-label="Dark photo of hands holding a phone">
  <h2>Fill Up The Form To Get Link For Downloading Sample Apps</h2>
  <div class="stores">
    <span class="store"><i></i>AppVault</span>
    <span class="store"><i></i>PlayCrate</span>
  </div>
</section>

<section class="contact">
  <span class="mail-badge"><svg width="40" height="28" viewBox="0 0 40 28"><rect x="1" y="1" width="38" height="26" rx="2" fill="#fff"/><path d="M2 3l18 13L38 3" fill="none" stroke="#2b2b2b" stroke-width="2.5"/></svg></span>
  <form class="lead-form">
    <div class="field">Your Name</div>
    <div class="field">Your Email</div>
    <div class="field wide">Subject</div>
    <div class="field wide message">Message</div>
    <div class="submit">Submit</div>
  </form>
</section>

<footer class="site-footer">
  <div class="wrap">
    <p class="copyright">Copyright © 2016 Brellowmo Media. All Rights Reserved.</p>
    <div class="social">
      <span class="s1">K</span><span class="s2">V</span><span class="s3">R</span><span class="s4">L</span>
    </div>
  </div>
</footer>

</body>
</html>
```